Business Card Design Project

Hi I am after a business card double sided 1 side to have the attached PDF on front on the back:

Tavi Rundell - Managing Director
Mobile: 0412 638 274
email: tavi@pruvo.com.au
web: www.pruvo.com.au

Industry/Entity Type

Business

Font styles to use
Sans Serif

Requirements
Must have
• I want a classy looking card
Nice to have
• I like lime green and black and white

```html
<!DOCTYPE html>
<html lang="en">
<head>
<meta charset="utf-8">
<title>Pruvo Lawns and Gardens – Business Card Front</title>
<link href="https://fonts.googleapis.com/css2?family=Questrial&display=swap" rel="stylesheet">
<style>
  :root {
    --backdrop: #d1d2d4;
    --card-black: #000000;
    --brand-green: #29b34b;
    --url-green: #3aa655;
    --text-white: #ffffff;
  }
  html, body {
    margin: 0;
    padding: 0;
    width: 1200px;
    height: 986px;
    overflow: hidden;
    background: var(--backdrop);
  }
  .stage {
    position: relative;
    width: 1200px;
    height: 986px;
  }
  .card-front {
    position: absolute;
    left: 68px;
    top: 185px;
    width: 1049px;
    height: 629px;
    background: var(--card-black);
    font-family: "Questrial", "Century Gothic", sans-serif;
  }
  .brand-mark {
    position: absolute;
    left: 447px;
    top: 164px;
    width: 155px;
    height: 155px;
    border-radius: 16px;
    background: var(--brand-green);
  }
  .brand-name {
    position: absolute;
    left: 0;
    top: 334px;
    width: 100%;
    margin: 0;
    text-align: center;
    color: var(--text-white);
    font-size: 45px;
    font-weight: 400;
    line-height: 1.2;
  }
  .web-address {
    position: absolute;
    left: 0;
    top: 456px;
    width: 100%;
    margin: 0;
    text-align: center;
    color: var(--url-green);
    font-size: 40px;
    letter-spacing: 3px;
    line-height: 1.2;
  }
</style>
</head>
<body>
  <div class="stage">
    <section class="card-front">
      <div class="brand-mark"></div>
      <h1 class="brand-name">Pruvo Lawns and Gardens</h1>
      <p class="web-address">www.pruvo.com.au</p>
    </section>
  </div>
</body>
</html>
```